Kestrelwood Pathways Agency business cards

Australian company about to start offering its services. We recruit international students to come to study English, vocational education and postgraduate courses in Australia. We help them find the institution and select the right city they want to come to Australia. We are a young, online oriented and supportive agency. Our clients are between 18 and 35 years old, mainly University students, young professionals or people with work experience. We provide much more information that any other agency offer. We administrate a Facebook group with more than 11.000 members that daily ask questions about general information when coming to Australia, while they are here and even after they leave the country

Target Market(s)

International students from South America, Central America and Europe

Industry/Entity Type

Student

Contact Information for Business Card

Tomas Brevik
Managing Director
tomas@velmorin.com.au
www.velmorin.com.au
+61 491058263
Melbourne, Australia

Font styles to use
Serif
Sans Serif

Colors

Designer to choose colors to be used in the design.

Requirements
Must have
• Horizontal design
• Standard business card size and shape. If font uses green or yellow colours, they will have to match the ones from the logo
Nice to have
• UPDATE: Use the contents of the green image to design one of the card sides. Use our logo in the background of that side as watermark.
• Passport image, or immigration stamps. A picture of the Yarra River (from Melbourne) would be cool as well.
Should not have
• Non-standard business card size and shape
• Not black as the background colour of any sides as we are not a VIP agency or a hight class service. We are orientes to young people and they like colours, pictures, something attractive.
• Vertical design
• NO YELLOW or BLACK AS THE BACKGROUND COLOUR OF ANY SIDE OF THE BIZ CARD

```html
<!DOCTYPE html>
<html lang="en">
<head>
<meta charset="utf-8">
<title>Kestrelwood Pathways Agency business cards</title>
<link rel="stylesheet" href="https://fonts.googleapis.com/css2?family=Arimo:wght@400;700&display=swap">
<style>
  :root {
    --page-bg: #e9eaea;
    --brand-green: #1f6b3c;
    --brand-yellow: #e8c21c;
    --ink: #2b2b2b;
    --front-bg-a: #f4f8f5;
    --front-bg-b: #e4eee8;
    --back-bg-a: #fbf7f7;
    --back-bg-b: #efe6e8;
    --stamp-green: rgba(120, 170, 150, 0.28);
    --stamp-red: rgba(210, 120, 130, 0.22);
  }
  * { box-sizing: border-box; margin: 0; padding: 0; }
  html, body { width: 1200px; height: 997px; overflow: hidden; }
  body {
    background: var(--page-bg);
    font-family: "Arimo", Arial, sans-serif;
    color: var(--ink);
    display: flex;
    flex-direction: column;
    align-items: center;
    justify-content: center;
    gap: 60px;
  }
  .card {
    position: relative;
    width: 700px;
    height: 400px;
    border-radius: 22px;
    overflow: hidden;
    box-shadow: 0 6px 18px rgba(0,0,0,0.15);
  }
  .card-front { background: linear-gradient(135deg, var(--front-bg-a), var(--front-bg-b)); }
  .card-back { background: linear-gradient(135deg, var(--back-bg-a), var(--back-bg-b)); }

  .stamp-field {
    position: absolute;
    inset: 0;
  }
  .card-front .stamp-field {
    background:
      radial-gradient(circle at 22% 78%, var(--stamp-green) 0 90px, transparent 92px),
      radial-gradient(circle at 78% 22%, var(--stamp-green) 0 70px, transparent 72px),
      radial-gradient(circle at 10% 30%, var(--stamp-red) 0 40px, transparent 42px);
  }
  .card-back .stamp-field {
    background:
      radial-gradient(circle at 84% 20%, var(--stamp-green) 0 80px, transparent 82px),
      radial-gradient(circle at 28% 40%, var(--stamp-red) 0 75px, transparent 77px),
      radial-gradient(circle at 70% 70%, var(--stamp-red) 0 70px, transparent 72px),
      radial-gradient(circle at 20% 85%, var(--stamp-green) 0 60px, transparent 62px);
  }

  .brand-name {
    position: absolute;
    font-weight: 700;
    color: var(--brand-green);
    letter-spacing: 1px;
  }
  .card-front .brand-name {
    left: 0; right: 0; top: 130px;
    text-align: center;
    font-size: 84px;
  }
  .front-url {
    position: absolute;
    right: 48px; bottom: 40px;
    font-size: 24px;
    font-weight: 700;
    color: var(--brand-green);
  }

  .card-back .brand-name {
    left: 0; right: 0; top: 54px;
    text-align: center;
    font-size: 60px;
  }
  .divider {
    position: absolute;
    left: 0; right: 0; top: 190px;
    height: 2px;
    background: var(--brand-green);
  }
  .person {
    position: absolute;
    left: 40px; top: 214px;
  }
  .person-name {
    font-size: 22px;
    font-weight: 700;
    color: var(--brand-green);
    letter-spacing: 0.5px;
  }
  .person-role { font-size: 18px; margin-top: 4px; }
  .contacts {
    position: absolute;
    left: 40px; bottom: 36px;
    list-style: none;
    font-size: 20px;
  }
  .contacts li { display: flex; align-items: center; gap: 12px; margin-top: 8px; }
  .contact-icon {
    width: 22px; height: 22px;
    border-radius: 50%;
    background: var(--brand-green);
    display: flex; align-items: center; justify-content: center;
  }
  .company {
    position: absolute;
    right: 40px; top: 214px;
    text-align: right;
    font-size: 18px;
    line-height: 1.35;
  }
  .company-name {
    font-weight: 700;
    color: var(--brand-green);
    letter-spacing: 0.5px;
  }
</style>
</head>
<body>
  <section class="card card-front">
    <div class="stamp-field" role="img" aria-label="Faint passport immigration stamps with brand watermark"></div>
    <div class="brand-name">Velmorin</div>
    <div class="front-url">www.velmorin.com.au</div>
  </section>

  <section class="card card-back">
    <div class="stamp-field" role="img" aria-label="Passport page with approved immigration stamps"></div>
    <div class="brand-name">Velmorin</div>
    <div class="divider"></div>
    <div class="person">
      <div class="person-name">TOMAS BREVIK</div>
      <div class="person-role">Managing Director</div>
    </div>
    <div class="company">
      <div class="company-name">VELMORIN PVT LTD.</div>
      <div>22 Harwick Lane, Box 310,</div>
      <div>Melbourne, Australia 3004</div>
    </div>
    <ul class="contacts">
      <li>
        <span class="contact-icon">
          <svg width="12" height="12" viewBox="0 0 24 24"><path fill="#fff" d="M6.6 10.8a15 15 0 0 0 6.6 6.6l2.2-2.2a1 1 0 0 1 1-.25 11.4 11.4 0 0 0 3.6.57 1 1 0 0 1 1 1V20a1 1 0 0 1-1 1A17 17 0 0 1 3 4a1 1 0 0 1 1-1h3.5a1 1 0 0 1 1 1c0 1.25.2 2.45.57 3.6a1 1 0 0 1-.25 1z"/></svg>
        </span>
        +61 491058263
      </li>
      <li>
        <span class="contact-icon">
          <svg width="12" height="12" viewBox="0 0 24 24"><path fill="#fff" d="M3 5h18v14H3zm2 2v.5l7 4.5 7-4.5V7z"/></svg>
        </span>
        tomas@velmorin.com.au
      </li>
    </ul>
  </section>
</body>
</html>
```